Local fast-growing company in the service sector

We are looking for a modern business card design, which should also appear on our letterheads

Target Market(s)

Private and industrial sectors

Contact Information for Business Card

Vorname Name
Lindkofer Str. 18
71468 Waiblingen
Tel.: 07163-418259-0
Name@kovaltec-pbz.de

Colors
9d9d9d
919191
aaaaaa

Requirements
Must have
• The logo (file) in silver

```html
<!DOCTYPE html>
<html lang="de">
<head>
<meta charset="utf-8">
<title>PBZ – Visitenkarte</title>
<link href="https://fonts.googleapis.com/css2?family=Lato:wght@400;700;900&display=swap" rel="stylesheet">
<style>
  :root {
    --page-bg: #e4e4e2;
    --card-bg: #ffffff;
    --silver: #9d9d9d;
    --silver-mid: #919191;
    --silver-light: #aaaaaa;
    --map-tone: #efefef;
    --text-dark: #4a4a4a;
    --text-body: #333333;
    --divider: #c8c8c8;
  }
  * { box-sizing: border-box; margin: 0; padding: 0; }
  html, body {
    width: 1200px; height: 675px; overflow: hidden;
    background: var(--page-bg);
    font-family: "Lato", sans-serif;
  }
  .canvas {
    position: relative; width: 1200px; height: 675px;
  }
  .card {
    position: absolute; top: 160px;
    width: 540px; height: 350px;
    background: var(--card-bg);
    box-shadow: 0 4px 14px rgba(0,0,0,0.12);
    overflow: hidden;
  }
  .card--front { left: 40px; }
  .card--back { left: 620px; }

  .world-map {
    position: absolute; left: 40px; top: 40px;
    width: 460px; height: 240px;
    background: radial-gradient(ellipse at center, var(--map-tone) 0%, rgba(239,239,239,0.4) 60%, rgba(255,255,255,0) 100%);
  }

  .brand {
    position: absolute;
    display: flex; flex-direction: column; align-items: flex-start;
  }
  .brand__row { display: flex; align-items: center; gap: 14px; }
  .brand__mark {
    width: 44px; height: 44px; background: var(--silver-light);
  }
  .brand__name {
    font-weight: 900; font-size: 64px; line-height: 1;
    color: var(--silver); letter-spacing: 2px;
  }
  .brand__web {
    font-weight: 700; font-size: 22px; color: var(--silver-mid);
    margin-left: 58px; margin-top: 2px; letter-spacing: 1px;
  }
  .card--front .brand { left: 120px; top: 115px; }
  .card--back .brand { left: 230px; top: 60px; }

  .back-accent {
    position: absolute; left: -70px; top: 60px;
    width: 200px; height: 200px; border-radius: 50%;
    background: #f3f3f3;
  }

  .holder-name {
    position: absolute; left: 40px; top: 232px;
    font-weight: 700; font-size: 17px; color: var(--text-dark);
    letter-spacing: 0.5px;
  }
  .contact-divider {
    position: absolute; left: 212px; top: 222px;
    width: 1px; height: 80px; background: var(--divider);
  }
  .contact-list {
    position: absolute; left: 226px; top: 226px;
    list-style: none;
    font-size: 15px; color: var(--text-body); line-height: 24px;
  }
  .contact-list li { display: flex; align-items: center; gap: 7px; }
  .contact-list svg { width: 14px; height: 14px; flex: none; }
</style>
</head>
<body>
<div class="canvas">

  <section class="card card--front" aria-label="Vorderseite">
    <div class="world-map" role="img" aria-label="Gepunktete Weltkarte im Hintergrund"></div>
    <div class="brand">
      <div class="brand__row">
        <span class="brand__mark"></span>
        <span class="brand__name">PBZ</span>
      </div>
      <span class="brand__web">kovaltec-pbz.de</span>
    </div>
  </section>

  <section class="card card--back" aria-label="Rückseite">
    <span class="back-accent"></span>
    <div class="brand">
      <div class="brand__row">
        <span class="brand__mark"></span>
        <span class="brand__name">PBZ</span>
      </div>
      <span class="brand__web">kovaltec-pbz.de</span>
    </div>

    <p class="holder-name">VORNAME NAME</p>
    <span class="contact-divider"></span>
    <ul class="contact-list">
      <li>
        <svg viewBox="0 0 14 14" aria-hidden="true"><circle cx="7" cy="7" r="7" fill="#9d9d9d"/><path d="M4.5 3.5l1.5 0 .6 1.8-.9.7a5 5 0 0 0 2.3 2.3l.7-.9 1.8.6v1.5c-3.4.3-6.3-2.6-6-6z" fill="#fff"/></svg>
        07163-418259-0
      </li>
      <li>
        <svg viewBox="0 0 14 14" aria-hidden="true"><circle cx="7" cy="7" r="7" fill="#9d9d9d"/><rect x="3.5" y="4.5" width="7" height="5" fill="#fff"/><path d="M3.5 4.5L7 7.3l3.5-2.8" fill="none" stroke="#9d9d9d" stroke-width="0.8"/></svg>
        name@kovaltec-pbz.de
      </li>
      <li>
        <svg viewBox="0 0 14 14" aria-hidden="true"><circle cx="7" cy="7" r="7" fill="#9d9d9d"/><path d="M7 3a2.5 2.5 0 0 0-2.5 2.5C4.5 7.5 7 11 7 11s2.5-3.5 2.5-5.5A2.5 2.5 0 0 0 7 3z" fill="#fff"/><circle cx="7" cy="5.5" r="0.9" fill="#9d9d9d"/></svg>
        Lindkofer Str. 18, 71468 Waiblingen
      </li>
    </ul>
  </section>

</div>
</body>
</html>
```